Executive Coaching Consultancy Website Design

I am setting up an executive coaching consultancy practice, primarily targeting ambitious women (and men of course!) who want to progress to the next level in their careers (late 20's to mid forties in age) or who are returning to work after a career break. I need a simple website that promotes the benefits of my consultancy service, contact details plus other associated information and incorporates social media channels so I can update information and news items on a regular basis. It would be useful to have a design for a Worknest dedicated page too.

This project has been on the back burner for a while due to other commitments, however when I originally decided to set the business up a couple of years ago, I did get a logo and some illustrations for the website designed and produced - which I've uploaded.

The design should convey expertise, understanding, serenity and trust. I am keen it appears stylish and different to many of the other coaching websites that use typical business imagery and are very cluttered. I am targeting individuals who want to invest their own time and money into getting to the next step (as opposed to targeting HR teams in large organisations).

The design should also be responsive so the target audience can easily view it on their phones/tablets.

Initially the information to be conveyed on the website will include:

- How coaching can improve career performance
- The coaching process and what to expect
- Fees
- About us
- Contact details
- A Blog
- Links to useful articles/organisations

etc.

A simple scroll down format would make sense but I will leave it to your best judgement!

Many thanks!!

Reason: Realised it was still the holiday period but am keen to receive prospective designs so I can commission this project quickly. Thanks!

Target Market(s)

28-45 yr old career women

Industry/Entity Type

Business

Number of Pages Required

2 page

Requirements
Must have
• Clean, simple intuitive navigation that can be adapted easily for responsive design purposes
Nice to have
• Area for testimonials
Should not have
• Cluttered information.

```html
<!DOCTYPE html>
<html lang="en">
<head>
<meta charset="utf-8">
<title>Halden Reed Coaching</title>
<link href="https://fonts.googleapis.com/css2?family=Open+Sans:wght@300;400;600&display=swap" rel="stylesheet">
<style>
:root{
  --ink:#333;
  --muted:#777;
  --faint:#aaa;
  --panel:#f2f2f2;
  --accent:#e0412f;
  --accent-dark:#c2301f;
  --link:#2aa3d8;
  --icon:#333;
  --white:#fff;
}
*{box-sizing:border-box;margin:0;padding:0}
html,body{width:674px;height:1200px;overflow:hidden;background:var(--white);font-family:'Open Sans',sans-serif;color:var(--ink)}
.page{position:absolute;left:150px;top:0;width:375px;height:1200px}
section,header,footer{position:relative;width:375px;overflow:hidden}
.abs{position:absolute}

/* neutral social icon slots */
.social-row{display:flex;align-items:center;justify-content:center}
.social-slot{display:block;border:0.8px solid var(--icon);border-radius:50%}

/* header */
.site-header{height:38px}
.brand{left:16px;top:11px}
.brand-name{font-size:5px;font-weight:600;color:#555;letter-spacing:.5px;text-transform:uppercase;line-height:6px}
.main-nav{left:157px;top:18px;display:flex;gap:13px}
.main-nav a{font-size:3.4px;font-weight:600;color:#444;text-decoration:none;letter-spacing:.3px;line-height:4px}
.header-social{left:330px;top:18px;gap:7px}
.header-social .social-slot{width:4.5px;height:4.5px;border-color:var(--link)}

/* hero */
.hero{height:176px}
.hero-photo{inset:0;background:radial-gradient(ellipse at 55% 45%,#8d8e88 0%,#4a4339 40%,#2a2520 100%)}
.hero-text{left:0;right:0;top:58px;text-align:center;color:var(--white)}
.hero-text h1{font-weight:300;font-size:12.5px;line-height:17px;padding:0 20px}
.hero-text p{font-size:4.2px;font-weight:600;margin-top:7px}

/* services */
.services{height:166px;background:var(--panel)}
.section-title{left:0;right:0;text-align:center;font-weight:300;font-size:9.5px;line-height:12px;color:#444}
.service{width:170px;display:flex;gap:14px}
.service svg{flex:none}
.service-body{width:124px}
.service h3{font-size:4.8px;font-weight:600;margin-bottom:4px;line-height:6px}
.service p{font-size:3.9px;line-height:6.8px;color:var(--faint)}

/* news */
.news{height:170px}
.news-item{width:110px}
.news-photo{width:81px;height:54px;background:linear-gradient(135deg,#c9cdd2,#6e7680 60%,#2f3338)}
.news-item h3{font-weight:300;font-size:6.9px;line-height:10px;color:#666;margin-top:9px}
.read-more{display:inline-block;margin-top:3px;font-size:3px;font-weight:600;color:var(--link);border-bottom:.6px solid var(--link);padding-bottom:1px;text-decoration:none}

/* testimonial */
.testimonial{height:140px}
.testimonial-photo{inset:0;background:linear-gradient(120deg,#6f7780 0%,#a59a92 55%,#8c7566 100%)}
.testimonial blockquote{left:16px;right:20px;top:47px;color:var(--white);font-size:11.2px;line-height:14.5px}

/* team */
.team{height:280px}
.team-intro{left:0;right:0;top:53px;text-align:center;font-size:3.8px;color:var(--muted)}
.member{width:70px;text-align:center}
.avatar{width:50px;height:50px;border-radius:50%;margin:0 auto;background:radial-gradient(circle at 50% 40%,#d8d8d8,#b8b8b8)}
.member h3{font-size:4.8px;font-weight:400;margin-top:6px;line-height:6px}
.member p{font-size:3.4px;color:var(--faint);margin-top:2px;line-height:4px}
.member .social-row{margin-top:4px;gap:7px}
.member .social-slot{width:4.5px;height:4.5px}

/* stats */
.stats{height:120px}
.stats-photo{inset:0;background:linear-gradient(180deg,#6c7b82 0%,#c0ad90 55%,#4f463d 100%)}
.stats .section-title{color:var(--white);top:26px;font-size:8.4px}
.stat{width:80px;text-align:center;color:var(--white)}
.stat-ring{width:35px;height:35px;border:1.4px solid var(--white);border-radius:50%;margin:0 auto;display:flex;align-items:center;justify-content:center;font-size:11px}
.stat p{font-size:7.5px;margin-top:4px;font-weight:300;line-height:10px}

/* contact row */
.contact-row{height:54px}
.contact-btn{left:16px;top:22px;width:46px;height:12px;border:.8px solid #555;border-radius:6px;font-size:3px;font-weight:600;display:flex;align-items:center;justify-content:center;letter-spacing:.3px;color:var(--ink)}
.contact-social{right:16px;top:24px;gap:8px}
.contact-social .social-slot{width:7px;height:7px;border-width:1px}

/* footer */
.site-footer{height:54px;background:var(--accent);color:var(--white)}
.footer-info{top:25px;font-size:3.6px;line-height:4px;white-space:nowrap}
.footer-info strong{font-weight:600}
.footer-cta{right:0;top:0;width:94px;height:54px;background:var(--accent-dark);display:flex;align-items:center;justify-content:center;font-size:4.6px;gap:3px;white-space:nowrap}
</style>
</head>
<body>
<div class="page">

  <header class="site-header">
    <div class="abs brand"><span class="brand-name">Halden Reed<br>Coaching</span></div>
    <nav class="abs main-nav">
      <a href="#">HOME</a><a href="#">SERVICES</a><a href="#">NEWS</a><a href="#">TESTIMONIALS</a><a href="#">TEAM</a><a href="#">CONTACT</a>
    </nav>
    <div class="abs social-row header-social"><span class="social-slot" aria-label="Social link"></span><span class="social-slot" aria-label="Social link"></span><span class="social-slot" aria-label="Social link"></span></div>
  </header>

  <section class="hero">
    <div class="abs hero-photo" role="img" aria-label="Kayaker paddling through white water beneath a rock arch"></div>
    <div class="abs hero-text">
      <h1>Facing hardships is the most horrible thing, we are here to help you out</h1>
      <p>We go the extra mile</p>
    </div>
  </section>

  <section class="services">
    <h2 class="abs section-title" style="top:24px">The services we provide</h2>
    <div class="abs service" style="left:29px;top:52px">
      <svg width="16" height="16" viewBox="0 0 16 16" fill="none" stroke="var(--accent)" stroke-width=".8"><ellipse cx="8" cy="8" rx="7" ry="3"/><ellipse cx="8" cy="8" rx="7" ry="3" transform="rotate(60 8 8)"/><ellipse cx="8" cy="8" rx="7" ry="3" transform="rotate(-60 8 8)"/><circle cx="8" cy="8" r="1"/></svg>
      <div class="service-body"><h3>Consulting Solutions</h3><p>Nam libero tempore, cum soluta nobis est eligendi optio cumque nihil impedit quo minus id quod maxime placeat facere possimus.</p></div>
    </div>
    <div class="abs service" style="left:204px;top:52px">
      <svg width="18" height="16" viewBox="0 0 18 16" fill="none" stroke="var(--accent)" stroke-width=".8"><polyline points="1,14 6,7 10,10 17,2"/><circle cx="6" cy="7" r="1"/><circle cx="10" cy="10" r="1"/></svg>
      <div class="service-body" style="padding-top:5px"><h3>Consulting Solutions</h3><p>Nam libero tempore, cum soluta nobis est eligendi optio cumque nihil impedit quo minus id quod maxime placeat facere possimus.</p></div>
    </div>
    <div class="abs service" style="left:29px;top:108px">
      <svg width="16" height="16" viewBox="0 0 16 16" fill="none" stroke="var(--accent)" stroke-width=".8"><line x1="2" y1="2" x2="14" y2="14"/><line x1="14" y1="2" x2="2" y2="14"/><circle cx="2.5" cy="2.5" r="1.5"/><circle cx="13.5" cy="2.5" r="1.5"/></svg>
      <div class="service-body"><h3>Consulting Solutions</h3><p>Nam libero tempore, cum soluta nobis est eligendi optio cumque nihil impedit quo minus id quod maxime placeat facere possimus.</p></div>
    </div>
    <div class="abs service" style="left:204px;top:108px">
      <svg width="18" height="16" viewBox="0 0 18 16" fill="none" stroke="var(--accent)" stroke-width=".8"><rect x="1" y="1" width="16" height="10"/><line x1="9" y1="11" x2="9" y2="14"/><line x1="5" y1="14" x2="13" y2="14"/></svg>
      <div class="service-body"><h3>Consulting Solutions</h3><p>Nam libero tempore, cum soluta nobis est eligendi optio cumque nihil impedit quo minus id quod maxime placeat facere possimus.</p></div>
    </div>
  </section>

  <section class="news">
    <h2 class="abs section-title" style="top:24px">Latest News &amp; Views</h2>
    <article class="abs news-item" style="left:16px;top:52px">
      <div class="news-photo" role="img" aria-label="Colleagues in a business meeting"></div>
      <h3>Why is building with us is so darn fun and dead-easy?</h3>
      <a class="read-more" href="#">READ MORE</a>
    </article>
    <article class="abs news-item" style="left:133px;top:52px">
      <div class="news-photo" role="img" aria-label="Team discussing around a desk"></div>
      <h3>Why is building with us is so darn fun and dead-easy?</h3>
      <a class="read-more" href="#">READ MORE</a>
    </article>
    <article class="abs news-item" style="left:250px;top:52px">
      <div class="news-photo" role="img" aria-label="Colleagues in a business meeting"></div>
      <h3>Why is building with us is so darn fun and dead-easy?</h3>
      <a class="read-more" href="#">READ MORE</a>
    </article>
  </section>

  <section class="testimonial">
    <div class="abs testimonial-photo" role="img" aria-label="Soft blurred backdrop of a warm outdoor scene"></div>
    <blockquote class="abs">Facing hardships is the most horrible thing, with the help of the team under Halden, its been an amazing ride.</blockquote>
  </section>

  <section class="team">
    <h2 class="abs section-title" style="top:26px">We've a killer team at the helm</h2>
    <p class="abs team-intro">The reason you should select us that we have an amazing team that can help you out in each aspect</p>
    <div class="abs member" style="left:21px;top:72px"><div class="avatar" role="img" aria-label="Portrait placeholder"></div><h3>Tessa Lowe</h3><p>Founder &amp; CEO</p><div class="social-row"><span class="social-slot"></span><span class="social-slot"></span><span class="social-slot"></span></div></div>
    <div class="abs member" style="left:109px;top:72px"><div class="avatar" role="img" aria-label="Portrait placeholder"></div><h3>Mark Ellison</h3><p>Founder &amp; COO</p><div class="social-row"><span class="social-slot"></span><span class="social-slot"></span><span class="social-slot"></span></div></div>
    <div class="abs member" style="left:197px;top:72px"><div class="avatar" role="img" aria-label="Portrait placeholder"></div><h3>Nora Vale</h3><p>Lead Designer</p><div class="social-row"><span class="social-slot"></span><span class="social-slot"></span><span class="social-slot"></span></div></div>
    <div class="abs member" style="left:285px;top:72px"><div class="avatar" role="img" aria-label="Portrait placeholder"></div><h3>Iris Quint</h3><p>Product Designer</p><div class="social-row"><span class="social-slot"></span><span class="social-slot"></span><span class="social-slot"></span></div></div>
    <div class="abs member" style="left:21px;top:172px"><div class="avatar" role="img" aria-label="Portrait placeholder"></div><h3>Dana Holt</h3><p>Developer</p><div class="social-row"><span class="social-slot"></span><span class="social-slot"></span><span class="social-slot" aria-label="Worknest"></span></div></div>
    <div class="abs member" style="left:109px;top:172px"><div class="avatar" role="img" aria-label="Portrait placeholder"></div><h3>Dana Holt</h3><p>Developer</p><div class="social-row"><span class="social-slot"></span><span class="social-slot"></span><span class="social-slot" aria-label="Worknest"></span></div></div>
    <div class="abs member" style="left:197px;top:172px"><div class="avatar" role="img" aria-label="Portrait placeholder"></div><h3>Dana Holt</h3><p>Developer</p><div class="social-row"><span class="social-slot"></span><span class="social-slot"></span><span class="social-slot" aria-label="Worknest"></span></div></div>
    <div class="abs member" style="left:285px;top:172px"><div class="avatar" role="img" aria-label="Portrait placeholder"></div><h3>Dana Holt</h3><p>Developer</p><div class="social-row"><span class="social-slot"></span><span class="social-slot"></span><span class="social-slot" aria-label="Worknest"></span></div></div>
  </section>

  <section class="stats">
    <div class="abs stats-photo" role="img" aria-label="Robed figure on a rocky summit above the clouds at sunrise"></div>
    <h2 class="abs section-title">More About Us</h2>
    <div class="abs stat" style="left:16px;top:52px"><div class="stat-ring">2500+</div><p>Our Clients</p></div>
    <div class="abs stat" style="left:104px;top:52px"><div class="stat-ring">2300+</div><p>Satisfied Clients</p></div>
    <div class="abs stat" style="left:192px;top:52px"><div class="stat-ring">1500</div><p>Current Clients</p></div>
    <div class="abs stat" style="left:280px;top:52px"><div class="stat-ring">0</div><p>Missed Deadlines</p></div>
  </section>

  <section class="contact-row">
    <a class="abs contact-btn" href="#">CONTACT US</a>
    <div class="abs social-row contact-social"><span class="social-slot" aria-label="Social link"></span><span class="social-slot" aria-label="Social link"></span><span class="social-slot" aria-label="Social link"></span></div>
  </section>

  <footer class="site-footer">
    <span class="abs footer-info" style="left:16px">© 2014 Inc.</span>
    <strong class="abs footer-info" style="left:58px">hello@haldenreed.net</strong>
    <span class="abs footer-info" style="left:109px">+123 4450 210</span>
    <span class="abs footer-info" style="left:156px">14 Linden Row 3000</span>
    <div class="abs footer-cta">
      <svg width="6" height="4" viewBox="0 0 6 4"><rect width="6" height="4" fill="var(--white)"/><polyline points="0,0 3,2.2 6,0" fill="none" stroke="var(--accent-dark)" stroke-width=".5"/></svg>
      <span>Get in touch with us</span>
      <svg width="6" height="4" viewBox="0 0 6 4" fill="none" stroke="var(--white)" stroke-width=".6"><line x1="0" y1="2" x2="5.5" y2="2"/><polyline points="3.8,0.4 5.5,2 3.8,3.6"/></svg>
    </div>
  </footer>

</div>
</body>
</html>
```